The Larkspur Initiative WEBSITE DESIGN

Larkspur is a not for profit working in international aid and development. The website needs to be lively not depressing,earthy rather than bling, have a dramatic impact over lightweight. It may be that a black and white with spot colour may be more impacting given the simplicity I want for the site. Larkspur works in partnership with registered NGOs in Asia and Africa. At any one time it will have about five feature projects. The purpose is for people to be able to find out about the projects, the countries, the partner organisations, people's stories and then give people the opportunity to give their financial and volunteer support.

Target Market(s)

First World Donors
All ages but particularly 25 - 55

Industry/Entity Type

Human Rights

Number of Pages Required

5+ page

Font styles to use
Sans Serif

Requirements
Must have
• Simplicity
• Easy access to giving options
• Highlight stories both video and image + copy (sample in attachments)
• Lots of images over copy
Nice to have
• Interest
• Not boring
• May work in black and white with a spot colour or sepia look
Should not have
• Shiny new look
• Dont know how many pages or if it be coded or uncoded - makes no sense to me

```html
<!DOCTYPE html>
<html lang="en">
<head>
<meta charset="utf-8">
<title>The Larkspur Initiative</title>
<link href="https://fonts.googleapis.com/css2?family=Open+Sans:wght@400;600;700&family=Oswald:wght@400;500;600&display=swap" rel="stylesheet">
<style>
:root{
  --ink:#2b2b2b;
  --muted:#777;
  --light:#f4f2ef;
  --line:#e2ded8;
  --dark:#231d19;
  --dark-2:#2f2722;
  --sepia-1:#6e5640;
  --sepia-2:#a88a68;
  --sepia-3:#d6c3a6;
  --spot:#c46a2a;
  --white:#fff;
  --footer:#efefef;
  --bar:#2e2e2e;
}
*{box-sizing:border-box;margin:0;padding:0}
html,body{width:1200px;height:2584px;overflow:hidden}
body{font-family:"Open Sans",Arial,sans-serif;color:var(--ink);background:var(--white);font-size:13px;line-height:1.6;position:relative}
h1,h2,h3,h4{font-weight:400}
a{text-decoration:none}
.wrap{width:1000px;margin:0 auto;position:relative}

/* header */
.site-header{height:120px;background:var(--white);border-bottom:1px solid var(--line)}
.brand{position:absolute;left:0;top:22px;display:flex;align-items:center;gap:10px}
.brand-dot{width:40px;height:40px;border-radius:50%;background:var(--spot)}
.brand-name{font-family:"Open Sans",sans-serif;font-weight:700;font-size:22px;color:var(--spot);letter-spacing:.5px}
.topbar{position:absolute;right:0;top:14px;display:flex;gap:22px;font-size:12px;color:var(--muted)}
.topbar span{display:flex;align-items:center;gap:6px}
.main-nav{position:absolute;right:0;top:70px;display:flex}
.main-nav a{display:block;padding:10px 22px;font-size:12px;font-weight:600;color:var(--ink);letter-spacing:.5px}
.main-nav a.active{color:var(--spot);border-bottom:2px solid var(--spot)}

/* hero */
.hero{height:510px;position:relative;background:linear-gradient(180deg,#8f7458 0%,#b79a78 45%,#7a6048 100%)}
.hero-arrow{position:absolute;top:235px;width:34px;height:34px;border-radius:50%;background:rgba(0,0,0,.45);display:flex;align-items:center;justify-content:center}
.hero-arrow.prev{left:14px}.hero-arrow.next{right:14px}
.hero-caption{position:absolute;left:100px;top:155px;width:440px;padding:22px 26px;background:rgba(20,15,12,.72);color:var(--white)}
.hero-caption h1{font-family:"Oswald",sans-serif;font-size:34px;font-weight:500;letter-spacing:1px;line-height:1.1}
.hero-caption p{font-size:12px;margin:10px 0 16px;color:#e6ddd2}
.btn-outline{display:inline-block;border:1px solid var(--white);color:var(--white);padding:8px 18px;font-size:11px;font-weight:600;letter-spacing:1px}

/* welcome */
.welcome{height:390px;background:var(--light);padding-top:48px;text-align:center}
.section-title{font-family:"Open Sans",sans-serif;font-size:30px;color:var(--ink)}
.section-intro{width:860px;margin:14px auto 0;font-size:11.5px;color:var(--muted);line-height:1.7}
.feature-grid{display:flex;gap:20px;margin-top:34px}
.feature{flex:1;background:var(--white);height:150px;padding:22px 18px;box-shadow:0 2px 8px rgba(0,0,0,.07)}
.feature svg{display:block;margin:0 auto 12px}
.feature h3{font-size:12px;font-weight:600;letter-spacing:.5px}
.feature p{font-size:10.5px;color:var(--muted);margin-top:6px;line-height:1.55}

/* projects */
.projects{height:630px;background:linear-gradient(180deg,var(--dark) 0%,var(--dark-2) 100%);padding-top:62px;color:var(--white)}
.projects .section-title{color:var(--white);text-align:center;font-size:34px}
.rule{width:60px;height:2px;background:var(--spot);margin:12px auto 0}
.project-grid{display:flex;gap:20px;margin-top:50px}
.project{flex:1}
.project-photo{height:190px;border:3px solid #4a3c31}
.project h3{font-family:"Oswald",sans-serif;font-size:16px;letter-spacing:1px;margin-top:16px}
.project p{font-size:11px;color:#bfb3a6;margin-top:6px}
.read-more{display:inline-flex;align-items:center;gap:8px;font-size:11px;font-weight:600;letter-spacing:1px;margin-top:16px;color:var(--white)}
.read-more i{width:16px;height:16px;border:1px solid var(--white);border-radius:50%;display:inline-flex;align-items:center;justify-content:center}

/* news */
.news{height:430px;padding-top:34px}
.news-heading{font-family:"Oswald",sans-serif;font-size:20px;letter-spacing:1px}
.news-heading:after{content:"";display:block;width:40px;height:2px;background:var(--spot);margin-top:6px}
.news-body{display:flex;gap:40px;margin-top:22px}
.news-list{width:560px}
.news-item{display:flex;gap:18px;margin-bottom:22px}
.news-thumb{width:170px;height:125px;flex:none}
.news-item h4{font-size:14px;font-weight:600}
.news-meta{font-size:10px;color:var(--spot);margin:4px 0 6px}
.news-item p{font-size:11px;color:var(--muted)}
.video{width:400px;height:250px;position:relative;margin-top:10px}
.video-screen{position:absolute;inset:0 0 30px 0;background:linear-gradient(135deg,#9b8166,#d2bea1 60%,#8a6f55)}
.video-play{position:absolute;left:170px;top:80px;width:60px;height:60px;border-radius:50%;background:rgba(255,255,255,.85);display:flex;align-items:center;justify-content:center}
.video-controls{position:absolute;left:0;right:0;bottom:0;height:30px;background:#222;display:flex;align-items:center;gap:10px;padding:0 10px}
.video-track{flex:1;height:4px;background:#555;position:relative}
.video-track:before{content:"";position:absolute;left:0;top:0;height:4px;width:35%;background:var(--spot)}

/* giving banners */
.support{height:170px;display:flex;gap:20px}
.support-card{flex:1;height:150px;position:relative;padding:24px 28px;color:var(--white)}
.support-card.giving{background:linear-gradient(90deg,#3a2f28,#8d7257)}
.support-card.volunteer{background:linear-gradient(90deg,#b69b7b,#4a3b30);text-align:right}
.support-card h2{font-family:"Oswald",sans-serif;font-size:42px;font-weight:600;line-height:1;letter-spacing:1px}
.support-card span{display:inline-block;margin-top:12px;font-size:11px;font-weight:600;letter-spacing:1px;border-bottom:2px solid var(--spot)}

/* footer */
.site-footer{position:absolute;left:0;right:0;top:2290px;height:250px;background:var(--footer);padding-top:30px}
.footer-cols{display:flex;gap:40px}
.footer-col h4{font-size:12px;font-weight:700;letter-spacing:.5px;margin-bottom:12px}
.contact{width:250px}.events{width:260px}.signup{width:240px}
.contact li,.events li{list-style:none;font-size:11px;color:var(--muted);margin-bottom:8px;display:flex;gap:8px}
.events li{display:block}
.events em{display:block;font-style:normal;font-size:10px;color:var(--spot)}
.field{display:flex;margin-bottom:8px}
.field span{flex:1;height:28px;background:var(--white);border:1px solid var(--line);font-size:10px;color:#aaa;padding:6px 8px}
.field b{height:28px;background:var(--bar);color:var(--white);font-size:10px;padding:7px 10px;font-weight:600}
.footer-brand{flex:1;display:flex;flex-direction:column;align-items:center;padding-top:6px}
.footer-brand .brand-name{font-size:20px}
.socials{display:flex;gap:6px;margin-top:12px}
.socials i{width:18px;height:18px;background:#555;display:block}
.bottom-bar{position:absolute;left:0;right:0;top:2540px;height:44px;background:var(--bar);color:#aaa;font-size:10px;text-align:center;line-height:44px}
</style>
</head>
<body>

<header class="site-header">
  <div class="wrap">
    <div class="brand"><span class="brand-dot"></span><span class="brand-name">Larkspur</span></div>
    <div class="topbar">
      <span><svg width="12" height="12" viewBox="0 0 24 24"><path d="M6.6 10.8a15 15 0 0 0 6.6 6.6l2.2-2.2c.3-.3.7-.4 1-.2 1.1.4 2.3.6 3.6.6.6 0 1 .4 1 1V20c0 .6-.4 1-1 1A17 17 0 0 1 3 4c0-.6.4-1 1-1h3.5c.6 0 1 .4 1 1 0 1.3.2 2.5.6 3.6.1.3 0 .7-.2 1z" fill="#777"/></svg>Call us today +1 555 014 2286</span>
      <span><svg width="12" height="12" viewBox="0 0 24 24"><rect x="2" y="5" width="20" height="14" fill="none" stroke="#777" stroke-width="2"/><path d="M2 6l10 7 10-7" fill="none" stroke="#777" stroke-width="2"/></svg>info@larkspurinitiative.org</span>
    </div>
    <nav class="main-nav">
      <a class="active" href="#">HOME</a><a href="#">ABOUT US</a><a href="#">PROJECTS</a><a href="#">NEWSLETTERS</a><a href="#">EVENTS</a><a href="#">CONTACT US</a>
    </nav>
  </div>
</header>

<section class="hero" role="img" aria-label="Sepia group photograph of community members standing outside a village building">
  <span class="hero-arrow prev"><svg width="12" height="12" viewBox="0 0 12 12"><path d="M8 1 3 6l5 5" fill="none" stroke="#fff" stroke-width="2"/></svg></span>
  <span class="hero-arrow next"><svg width="12" height="12" viewBox="0 0 12 12"><path d="M4 1l5 5-5 5" fill="none" stroke="#fff" stroke-width="2"/></svg></span>
  <div class="hero-caption">
    <h1>LARKSPUR INITIATIVE</h1>
    <p>Working side by side with local partners in Asia and Africa to build lasting change in the communities they serve.</p>
    <span class="btn-outline">VIEW MORE INFO</span>
  </div>
</section>

<section class="welcome">
  <div class="wrap">
    <h2 class="section-title">Welcome To Larkspur Initiative</h2>
    <p class="section-intro">We are a not for profit partnering with registered grassroots organisations across Asia and Africa. Together we support education, health, clean water and fair livelihoods, listening first to the people who live the challenges every day. Explore our feature projects, meet our partners and read the stories of the families whose lives are changing, then find a way to give your time or support.</p>
    <div class="feature-grid">
      <div class="feature">
        <svg width="34" height="34" viewBox="0 0 24 24"><path d="M2 11 22 3l-6 18-4-7z M12 14l10-11" fill="none" stroke="#444" stroke-width="1.8" stroke-linejoin="round"/></svg>
        <h3>PURPOSE</h3>
        <p>Why we exist and the change we hope to see in every partner community.</p>
      </div>
      <div class="feature">
        <svg width="34" height="34" viewBox="0 0 24 24"><path d="M12 21s-8-5-8-11a4.5 4.5 0 0 1 8-2.8A4.5 4.5 0 0 1 20 10c0 6-8 11-8 11z" fill="#444"/></svg>
        <h3>VALUES</h3>
        <p>Respect, honesty and partnership guide each decision we make together.</p>
      </div>
      <div class="feature">
        <svg width="34" height="34" viewBox="0 0 24 24"><circle cx="12" cy="7" r="4.5" fill="#444"/><path d="M3 22c0-5 4-8 9-8s9 3 9 8z" fill="#444"/></svg>
        <h3>MEANING OF NAME</h3>
        <p>The story behind our name and the hope it carries for those we serve.</p>
      </div>
      <div class="feature">
        <svg width="34" height="34" viewBox="0 0 24 24"><path d="M2 9 12 3l10 6z" fill="#444"/><path d="M5 10v8M9.5 10v8M14.5 10v8M19 10v8" stroke="#444" stroke-width="2"/><rect x="2" y="19" width="20" height="2.5" fill="#444"/></svg>
        <h3>BOARD</h3>
        <p>Meet the volunteers who guide our work and keep us accountable.</p>
      </div>
    </div>
  </div>
</section>

<section class="projects">
  <div class="wrap">
    <h2 class="section-title">Our Projects</h2>
    <div class="rule"></div>
    <div class="project-grid">
      <article class="project">
        <div class="project-photo" role="img" aria-label="Sepia photo of children gathered in a classroom in Cambodia" style="background:linear-gradient(135deg,#6b533d,#b3946f)"></div>
        <h3>BRIGHTPATH CAMBODIA</h3>
        <p>Helping rural children stay in school through tutoring, meals and family support programs.</p>
        <span class="read-more">READ MORE <i><svg width="8" height="8" viewBox="0 0 8 8"><path d="M2 1l3 3-3 3" fill="none" stroke="#fff" stroke-width="1.4"/></svg></i></span>
      </article>
      <article class="project">
        <div class="project-photo" role="img" aria-label="Sepia portrait of a project worker in Rwanda" style="background:linear-gradient(135deg,#4f3d2f,#a1825f)"></div>
        <h3>HILLSIDE RWANDA</h3>
        <p>Training women in small business skills so they can earn a steady income at home.</p>
        <span class="read-more">READ MORE <i><svg width="8" height="8" viewBox="0 0 8 8"><path d="M2 1l3 3-3 3" fill="none" stroke="#fff" stroke-width="1.4"/></svg></i></span>
      </article>
      <article class="project">
        <div class="project-photo" role="img" aria-label="Sepia photo of villagers collecting water in Kenya" style="background:linear-gradient(135deg,#7d6148,#c8ad88)"></div>
        <h3>RIVERSTONE KENYA</h3>
        <p>Bringing clean water and sanitation to villages in the dry north of the country.</p>
        <span class="read-more">READ MORE <i><svg width="8" height="8" viewBox="0 0 8 8"><path d="M2 1l3 3-3 3" fill="none" stroke="#fff" stroke-width="1.4"/></svg></i></span>
      </article>
    </div>
  </div>
</section>

<section class="news">
  <div class="wrap">
    <h2 class="news-heading">NEWS / STORIES</h2>
    <div class="news-body">
      <div class="news-list">
        <article class="news-item">
          <div class="news-thumb" role="img" aria-label="Sepia photo of a mother and child" style="background:linear-gradient(135deg,#6e5640,#bfa27e)"></div>
          <div>
            <h4>A New School Year Begins</h4>
            <div class="news-meta">12 MARCH 2024 &nbsp;|&nbsp; 3 COMMENTS</div>
            <p>Forty new students joined our partner school this term, many of them the first in their family to learn to read and write.</p>
          </div>
        </article>
        <article class="news-item">
          <div class="news-thumb" role="img" aria-label="Sepia photo of a young girl smiling" style="background:linear-gradient(135deg,#8a6e52,#d0b895)"></div>
          <div>
            <h4>Water Well Completed</h4>
            <div class="news-meta">28 FEBRUARY 2024 &nbsp;|&nbsp; 5 COMMENTS</div>
            <p>A village of three hundred people now has safe drinking water just minutes from home, thanks to our generous donors.</p>
          </div>
        </article>
      </div>
      <div class="video">
        <div class="video-screen" role="img" aria-label="Video still of a story from a partner community"></div>
        <span class="video-play"><svg width="22" height="22" viewBox="0 0 22 22"><path d="M6 3l13 8-13 8z" fill="#333"/></svg></span>
        <div class="video-controls">
          <svg width="10" height="12" viewBox="0 0 10 12"><path d="M0 0l10 6-10 6z" fill="#fff"/></svg>
          <div class="video-track"></div>
          <span style="color:#ccc;font-size:10px">01:24</span>
        </div>
      </div>
    </div>
  </div>
</section>

<section class="wrap support">
  <a class="support-card giving" role="img" aria-label="Sepia photo of smiling children, online giving banner">
    <h2>ONLINE<br>GIVING</h2>
    <span>DONATE NOW</span>
  </a>
  <a class="support-card volunteer" role="img" aria-label="Sepia photo of volunteers, volunteer vacancies banner">
    <h2>VOLUNTEER<br>VACANCIES</h2>
    <span>GET INVOLVED</span>
  </a>
</section>

<footer class="site-footer">
  <div class="wrap footer-cols">
    <div class="footer-col contact">
      <h4>CONTACT US</h4>
      <ul>
        <li><svg width="12" height="14" viewBox="0 0 24 24"><path d="M12 2a7 7 0 0 0-7 7c0 5 7 13 7 13s7-8 7-13a7 7 0 0 0-7-7zm0 9.5A2.5 2.5 0 1 1 12 6.5a2.5 2.5 0 0 1 0 5z" fill="#777"/></svg>Larkspur Initiative<br>1420 Meadow Lane<br>Springfield, USA</li>
        <li><svg width="12" height="12" viewBox="0 0 24 24"><path d="M6.6 10.8a15 15 0 0 0 6.6 6.6l2.2-2.2c.3-.3.7-.4 1-.2 1.1.4 2.3.6 3.6.6.6 0 1 .4 1 1V20c0 .6-.4 1-1 1A17 17 0 0 1 3 4c0-.6.4-1 1-1h3.5c.6 0 1 .4 1 1 0 1.3.2 2.5.6 3.6.1.3 0 .7-.2 1z" fill="#777"/></svg>+1 555 014 2286</li>
        <li><svg width="12" height="12" viewBox="0 0 24 24"><rect x="2" y="5" width="20" height="14" fill="none" stroke="#777" stroke-width="2"/><path d="M2 6l10 7 10-7" fill="none" stroke="#777" stroke-width="2"/></svg>info@larkspurinitiative.org</li>
      </ul>
    </div>
    <div class="footer-col events">
      <h4>RECENT EVENTS</h4>
      <ul>
        <li>Community dinner raises funds for the new classroom project.<em>2 days ago</em></li>
        <li>Volunteers return from a month of service in Kenya.<em>5 days ago</em></li>
      </ul>
    </div>
    <div class="footer-col signup">
      <h4>SIGN UP FOR NEWSLETTER</h4>
      <div class="field"><span>Your Name</span></div>
      <div class="field"><span>Email Address</span><b>SUBSCRIBE</b></div>
    </div>
    <div class="footer-brand">
      <span class="brand-dot"></span>
      <span class="brand-name">Larkspur</span>
      <div class="socials"><i></i><i></i><i></i></div>
    </div>
  </div>
</footer>
<div class="bottom-bar">© 2024 – The Larkspur Initiative. All Rights Reserved.</div>

</body>
</html>
```